Mobile phone signal boosting solutions needs a website

We need a website design for the reselling of a mobile signal boosting product set. These solutions are Vexlor exempt and will provide an indoor signal for mobile phones. We would like to see designs that incorporate the colours and feel of our logo. The domain will be
openmeadow.com / co.uk
Overview of the company and how it is to be used: Open meadow (domain name) will work with business and end user to provide mobile signal boosting – where people struggle indoors with a mobile signal our solutions will help by finding the smallest signal and boosting it, allowing users to use voice and data over their mobile network (please note this is not wireless signal boosting)
Number of Pages:
-Home
-Solutions / How it works
-Case Studies
-Contact
Text content: Currently just use placeholders
Technical specs : Wordpress and ability to use CMS if that’s relevant
Target Market(s)
Business professional all markets /high end residential
Coded - Design and coding required
4 page

```html
<!DOCTYPE html>
<html lang="en">
<head>
<meta charset="utf-8">
<title>Open meadow – Mobile signal boosting</title>
<link href="https://fonts.googleapis.com/css2?family=Poppins:ital,wght@0,400;0,500;0,600;0,700;1,400&family=Open+Sans:wght@400;600&display=swap" rel="stylesheet">
<style>
:root{
  --yellow:#ffc400;
  --amber:#f6a800;
  --gold:#f4b400;
  --mustard:#efbf0f;
  --btn:#fcd20c;
  --ink:#141414;
  --text:#333;
  --muted:#777;
  --red:#e5542b;
  --blue:#1e90f0;
  --icon-blue:#cfe3f7;
  --icon-orange:#fde2bf;
  --white:#fff;
  --black:#0b0b0b;
}
*{margin:0;padding:0;box-sizing:border-box}
html,body{width:1200px;height:5076px;overflow:hidden;background:var(--white)}
body{position:relative;font-family:"Open Sans",sans-serif;color:var(--text)}
.abs{position:absolute}
h1,h2,h3,h4,.display{font-family:"Poppins",sans-serif;color:var(--ink)}
.brand{font-family:"Poppins",sans-serif;font-weight:600;color:var(--ink);display:flex;align-items:center;gap:8px;font-size:17px}
.brand i{display:block;width:12px;height:12px;background:var(--gold)}
/* header */
.site-header{left:0;top:0;width:1200px;height:84px;background:var(--white)}
.nav{left:290px;top:0;height:84px;display:flex;gap:22px;align-items:center;font-family:"Poppins",sans-serif;font-size:13px;color:#333}
.nav a{color:inherit;text-decoration:none;position:relative}
.nav a.active:after{content:"";position:absolute;left:0;right:0;bottom:-30px;height:2px;background:#333}
.header-icons{right:80px;top:30px;display:flex;gap:42px}
/* hero */
.hero{left:0;top:84px;width:1200px;height:680px;background:linear-gradient(180deg,var(--gold),var(--amber));overflow:hidden}
.hero-kicker{left:100px;top:205px;font-size:13px;color:#c9461b}
.hero h1{left:100px;top:230px;font-size:42px;line-height:1.2;font-weight:700;width:540px}
.hero-text{left:100px;top:350px;width:480px;font-size:13px;line-height:1.6;color:#c9461b}
.btn{display:inline-flex;align-items:center;justify-content:center;font-family:"Poppins",sans-serif;font-weight:600;color:var(--ink);background:var(--btn);text-decoration:none}
.hero .btn{left:100px;top:420px;width:126px;height:44px;font-size:11px}
.hero-photo{left:770px;top:60px;width:370px;height:620px;background:linear-gradient(160deg,#f1d3c0,#e6e6e6 50%,#b4a08d);border-radius:180px 180px 0 0}
.hero-badge{left:570px;top:76px;width:248px;height:248px;border-radius:50%;background:#fcd23f;display:flex;align-items:center;justify-content:center}
.hero-badge .brand{font-size:22px}
.round-arrow{width:52px;height:52px;border-radius:50%;border:2px solid rgba(255,255,255,.8);display:flex;align-items:center;justify-content:center}
.hero-wave{left:0;top:600px}
/* services */
.kicker{font-size:20px;color:#333}
.section-title{font-size:48px;font-weight:700}
.services-kicker{left:100px;top:840px}
.services-title{left:100px;top:875px}
.services-lead{left:100px;top:958px;width:480px;font-size:14px;line-height:1.7;color:#222}
.btn-small{left:928px;top:955px;width:170px;height:45px;font-size:12px;font-weight:500;border-radius:8px;background:var(--yellow)}
.service-card{top:1065px;width:230px;height:300px;background:var(--white);border-radius:8px;box-shadow:0 4px 16px rgba(0,0,0,.12);text-align:center}
.service-icon{width:88px;height:88px;margin:76px auto 0;border-radius:50%;background:linear-gradient(135deg,var(--icon-blue),var(--icon-orange))}
.service-card h3{margin-top:22px;font-size:20px;font-weight:600}
/* about */
.about{left:0;top:1440px;width:1200px;height:820px;background:linear-gradient(180deg,var(--yellow),var(--gold))}
.about-photo{left:0;top:90px;width:600px;height:630px;background:linear-gradient(135deg,#f7c21a,#f5f1e6 45%,#f2b106)}
.about-kicker{left:648px;top:222px;font-size:19px}
.about h2{left:646px;top:250px;font-size:38px;font-weight:700}
.about-sub{left:646px;top:320px;width:400px;font-family:"Poppins",sans-serif;font-style:italic;font-size:21px;line-height:1.3;color:var(--ink)}
.about-text{left:648px;top:398px;width:320px;font-size:13px;line-height:1.6;color:var(--ink)}
.skill{left:648px;width:395px;font-size:11px;font-weight:600;color:var(--ink)}
.skill .row{display:flex;justify-content:space-between}
.skill .track{margin-top:4px;height:6px;background:#fbe6a5;border-radius:3px}
.skill .fill{height:6px;background:var(--red);border-radius:3px}
/* case */
.label{font-size:11px;font-weight:600;color:var(--ink)}
.case-label{left:108px;top:2407px}
.case-title{left:108px;top:2426px;width:500px;font-size:40px;line-height:1.15;font-weight:500}
.case-text{left:112px;top:2582px;width:330px;font-size:12px;line-height:1.75;color:var(--ink)}
.more-tab{left:885px;top:2338px;width:207px;height:57px;font-size:13px;background:var(--yellow)}
.quote-card{left:608px;top:2395px;width:484px;height:330px;background:var(--white);box-shadow:0 4px 18px rgba(0,0,0,.12);padding:70px 76px;font-size:12px;line-height:1.9;color:#333}
.pager{display:flex;align-items:center;justify-content:space-between;margin-top:28px}
.pager .nums{display:flex;align-items:center;gap:14px}
.pager .nums b{display:block;width:42px;height:1px;background:#333}
.circle-btn{display:inline-flex;width:40px;height:40px;border-radius:50%;background:#f1f1f1;align-items:center;justify-content:center;margin-left:10px}
.video-photo{left:108px;top:2762px;width:484px;height:298px;background:linear-gradient(135deg,#d9d9d9,#f2f2f2 55%,#c8c8c8);box-shadow:0 4px 14px rgba(0,0,0,.15)}
.play{width:48px;height:48px;border-radius:50%;background:#1a1a1a;display:flex;align-items:center;justify-content:center}
.video-label{left:660px;top:2800px}
.video-title{left:660px;top:2827px;font-size:34px;line-height:1.1;font-weight:500}
.video-text{left:660px;top:2915px;width:330px;font-size:12px;line-height:1.75;color:var(--ink)}
/* faq */
.faq-band{left:0;top:3180px;width:1200px;height:335px;background:var(--mustard)}
.faq-couple{left:490px;top:3250px;width:210px;height:265px;background:linear-gradient(180deg,#e8c64c,#c48b3c)}
.faq-label{left:108px;top:3252px;font-size:11px;font-weight:600;color:var(--white)}
.faq-title{left:108px;top:3275px;font-size:34px;line-height:1.1;font-weight:500;color:var(--white)}
.faq-text{left:108px;top:3368px;width:330px;font-size:11px;line-height:1.7;color:var(--white)}
.faq-photo{left:0;top:3515px;width:700px;height:425px;background:linear-gradient(120deg,#7a5a44,#c9a07f 40%,#4a4a4a)}
.faq-panel{left:700px;top:3448px;width:500px;height:550px;background:#ffc400;padding:88px 56px 0 56px}
.faq-panel .play-row{display:flex;align-items:center;gap:10px;font-family:"Poppins",sans-serif;font-size:13px;color:var(--ink)}
.faq-panel h3{margin-top:20px;font-size:33px;line-height:1.1;font-weight:500}
.faq-list{margin-top:44px;font-size:12px;color:var(--ink);list-style:none}
.faq-list li{margin-bottom:26px}
.faq-list strong{font-weight:600}
.faq-list p{font-weight:400;line-height:1.8;width:300px;margin:18px 0 0 0}
/* contact */
.contact-label{left:108px;top:4060px}
.contact-title{left:108px;top:4085px;font-size:32px;font-weight:500}
.contact-text{left:108px;top:4138px;width:650px;font-size:11px;line-height:1.75;color:var(--ink)}
.info-title{font-family:"Poppins",sans-serif;font-size:19px;font-weight:500;color:var(--ink)}
.info-line{font-size:12px;line-height:1.9;color:#333}
.field{border-bottom:1px solid #ccc;height:34px;font-size:12px;color:#999;display:flex;align-items:center;gap:10px}
.send{left:915px;top:4485px;width:160px;height:44px;font-size:12px;color:var(--white);background:var(--blue);border-radius:4px}
.social{display:flex;gap:24px}
.social i{display:block;width:13px;height:13px;background:#444;border-radius:2px}
/* footer */
.footer{left:0;top:4625px;width:1200px;height:451px;background:var(--black);color:var(--white)}
.footer .brand{color:var(--white);font-size:22px}
.footer-contact{left:120px;top:170px;font-size:12px;line-height:1.6;color:#ddd}
.footer-contact div{display:flex;gap:14px;margin-bottom:16px;align-items:flex-start}
.f-col h4{font-size:15px;font-weight:600;color:var(--white)}
.f-col h4:after{content:"";display:block;width:44px;height:2px;background:var(--white);margin-top:10px}
.f-col ul{list-style:none;margin-top:18px;font-size:11px;color:#ddd}
.f-col li{margin-bottom:20px}
.footer .social i{background:#ddd;width:12px;height:12px}
.copy{left:120px;top:425px;font-size:11px;color:#ddd}
.cards{left:855px;top:380px;display:flex;gap:5px}
.cards i{display:block;width:55px;height:28px;border-radius:3px;background:#e9e9e9}
</style>
</head>
<body>

<header class="site-header abs">
  <div class="brand abs" style="left:100px;top:30px"><i></i>Open meadow</div>
  <nav class="nav abs">
    <a class="active">HOME</a><a>HOW IT WORKS</a><a>ABOUT US</a><a>LATEST PRODUCTS</a><a>CONTACT US</a>
  </nav>
  <div class="header-icons abs">
    <svg width="16" height="16" viewBox="0 0 16 16" fill="none" stroke="#f6a800" stroke-width="2"><circle cx="7" cy="7" r="5"/><path d="M11 11l4 4"/></svg>
    <svg width="18" height="18" viewBox="0 0 18 18" fill="none" stroke="#f6a800" stroke-width="2"><circle cx="9" cy="9" r="8"/><circle cx="9" cy="7" r="3"/></svg>
    <svg width="18" height="16" viewBox="0 0 18 16" fill="#f6a800"><path d="M0 1h3l2 9h10l2-7H5" fill="none" stroke="#f6a800" stroke-width="2"/><circle cx="7" cy="14" r="1.5"/><circle cx="14" cy="14" r="1.5"/></svg>
  </div>
</header>

<section class="hero abs">
  <p class="hero-kicker abs">Lorem ipsum dolor sit amet, consectetur adipiscing elit!</p>
  <h1 class="abs">Lorem ipsum dolor<br>sit amet, consectetur.</h1>
  <p class="hero-text abs">Lorem ipsum dolor sit amet, consectetur adipiscing elit, sed do eiusmod tempor incididunt ut labore et dolore magna aliqua. Ut</p>
  <a class="btn abs">LEARN MORE</a>
  <div class="hero-photo abs" role="img" aria-label="Smiling woman in a striped shirt pointing at the brand badge"></div>
  <div class="hero-badge abs"><div class="brand"><i></i>Open meadow</div></div>
  <div class="round-arrow abs" style="left:34px;top:310px"><svg width="18" height="14" fill="none" stroke="#fff" stroke-width="2"><path d="M17 7H2M8 1L2 7l6 6"/></svg></div>
  <div class="round-arrow abs" style="left:1114px;top:310px"><svg width="18" height="14" fill="none" stroke="#fff" stroke-width="2"><path d="M1 7h15M10 1l6 6-6 6"/></svg></div>
  <svg class="abs" style="left:582px;top:565px" width="36" height="54" fill="none" stroke="#fff" stroke-width="2"><rect x="2" y="2" width="32" height="50" rx="16"/><path d="M18 14v10"/></svg>
  <svg class="hero-wave abs" width="1200" height="80" viewBox="0 0 1200 80" preserveAspectRatio="none"><path d="M0 55C200 15 350 10 520 40C700 72 900 30 1200 35V80H0Z" fill="#fff"/></svg>
</section>

<section>
  <p class="kicker services-kicker abs">What we do?</p>
  <h2 class="section-title services-title abs">Our Services</h2>
  <p class="services-lead abs">Lorem ipsum dolor sit amet, consectetur adipiscing elit,<br>sed do eiusmod tempor incididunt ut labore.</p>
  <a class="btn btn-small abs">View All Services</a>

  <div class="service-card abs" style="left:100px">
    <div class="service-icon" role="img" aria-label="Free trial service icon"></div>
    <h3>Free Trial</h3>
  </div>
  <div class="service-card abs" style="left:355px">
    <div class="service-icon" role="img" aria-label="Secure data service icon"></div>
    <h3>Secure Data</h3>
  </div>
  <div class="service-card abs" style="left:613px">
    <div class="service-icon" role="img" aria-label="Quick access service icon"></div>
    <h3>Quick Access</h3>
  </div>
  <div class="service-card abs" style="left:870px">
    <div class="service-icon" role="img" aria-label="Round-the-clock support service icon"></div>
    <h3>24h Support</h3>
  </div>
</section>

<section class="about abs">
  <svg class="abs" style="left:0;top:-1px" width="1200" height="70" viewBox="0 0 1200 70" preserveAspectRatio="none"><path d="M0 0H1200V20C1000 55 800 0 600 20C400 45 200 55 0 30Z" fill="#fff"/></svg>
  <div class="about-photo abs" role="img" aria-label="White signal booster unit with antennas on a yellow surface"></div>
  <p class="about-kicker abs">About Us</p>
  <h2 class="abs">Who we are?</h2>
  <p class="about-sub abs">Lorem ipsum dolor sit amet,<br>consectetur adipiscing elit,</p>
  <p class="about-text abs">Lorem ipsum dolor sit amet, consectetur adipiscing elit, sed do eiusmod tempor incididunt ut labore et dolore magna aliqua.</p>
  <div class="skill abs" style="top:505px"><div class="row"><span>Lorem ipsum</span><span>90%</span></div><div class="track"><div class="fill" style="width:90%"></div></div></div>
  <div class="skill abs" style="top:551px"><div class="row"><span>Lorem ipsum</span><span style="margin-right:15%">80%</span></div><div class="track"><div class="fill" style="width:80%"></div></div></div>
  <div class="skill abs" style="top:598px"><div class="row"><span>Lorem</span><span>85%</span></div><div class="track"><div class="fill" style="width:85%"></div></div></div>
  <svg class="abs" style="left:0;top:750px" width="1200" height="70" viewBox="0 0 1200 70" preserveAspectRatio="none"><path d="M0 40C250 10 450 60 700 35C900 15 1050 40 1200 25V70H0Z" fill="#fff"/></svg>
</section>

<section>
  <p class="label case-label abs">Case Statement</p>
  <h2 class="case-title abs">Lorem ipsum dolor<br>sit amet, consectetur<br>adipiscing elit, sed do!</h2>
  <p class="case-text abs">Lorem ipsum dolor sit amet, consectetur adipiscing elit, sed do eiusmod tempor incididunt ut labore et dolore magna aliqua. Ut enim ad minim veniam, quis nostrud exercitation ullamco laboris nisi ut aliquip ex ea commodo consequat.</p>
  <a class="btn more-tab abs">MORE INFO</a>
  <div class="quote-card abs">
    <p>Customer Support</p>
    <p style="margin-top:8px">“Lorem ipsum dolor sit amet, consectetur adipiscing elit, sed do eiusmod tempor incididunt ut labore et dolore magna aliqua. Ut enim ad minim veniam.”</p>
    <p style="margin-top:8px;line-height:1.6">Mara Quell<br>Co-founder, Company Name</p>
    <div class="pager">
      <div class="nums"><span>1</span><b></b><span>3</span></div>
      <div><span class="circle-btn"><svg width="14" height="10" fill="none" stroke="#222" stroke-width="1.6"><path d="M13 5H2M6 1L2 5l4 4"/></svg></span><span class="circle-btn"><svg width="14" height="10" fill="none" stroke="#222" stroke-width="1.6"><path d="M1 5h11M8 1l4 4-4 4"/></svg></span></div>
    </div>
  </div>

  <div class="video-photo abs" role="img" aria-label="Flat lay of a router, cables and signal symbols around a small house">
    <div class="play abs" style="left:218px;top:125px"><svg width="12" height="14"><path d="M0 0l12 7-12 7z" fill="#f6a800"/></svg></div>
  </div>
  <p class="label video-label abs">Lorem ipsum dolor sit</p>
  <h2 class="video-title abs">Lorem ipsum<br>dolor sit amet,</h2>
  <p class="video-text abs">Lorem ipsum dolor sit amet, consectetur adipiscing elit, sed do eiusmod tempor incididunt ut labore et dolore magna aliqua. Ut enim ad minim veniam, quis nostrud exercitation ullamco laboris nisi ut aliquip ex ea commodo consequat.</p>
</section>

<section>
  <div class="faq-band abs"></div>
  <div class="faq-couple abs" role="img" aria-label="Couple outdoors holding a phone up towards the sky"></div>
  <p class="faq-label abs">FAQs</p>
  <h2 class="faq-title abs">Lorem ipsum dolor<br>sit amet, consectetur!</h2>
  <p class="faq-text abs">Lorem ipsum dolor sit amet, consectetur adipiscing elit, sed do eiusmod tempor incididunt ut labore et dolore magna aliqua. Ut enim ad minim veniam, quis nostrud.</p>
  <div class="faq-photo abs" role="img" aria-label="Two friends on a sofa looking at a tablet"></div>
  <div class="faq-panel abs">
    <div class="play-row"><span class="play"><svg width="10" height="12"><path d="M0 0l10 6-10 6z" fill="#fff"/></svg></span>Play Video</div>
    <h3>Lorem ipsum dolor sit amet, consectetur adipiscing elit, sed</h3>
    <ul class="faq-list">
      <li><strong>—&nbsp;&nbsp; Lorem ipsum dolor sit amet</strong>
        <p>Lorem ipsum dolor sit amet, consectetur adipiscing elit, sed do eiusmod tempor incididunt ut labore et dolore magna aliqua. Ut</p></li>
      <li><strong>+&nbsp;&nbsp; Lorem ipsum dolor sit amet</strong></li>
      <li><strong>+&nbsp;&nbsp; Lorem ipsum dolor sit amet</strong></li>
    </ul>
  </div>
</section>

<section>
  <p class="label contact-label abs">Contact Us</p>
  <h2 class="contact-title abs">Lorem ipsum dolor sit amet, consectetur!</h2>
  <p class="contact-text abs">Lorem ipsum dolor sit amet, consectetur adipiscing elit, sed do eiusmod tempor incididunt ut labore et dolore magna aliqua. Ut enim ad minim veniam, quis nostrud. exercitation ullamco laboris nisi ut aliquip ex ea</p>
  <p class="info-title abs" style="left:110px;top:4218px">Visit our studio at</p>
  <p class="info-line abs" style="left:110px;top:4255px">48 Harlow Row, Unit 3,<br>Brindmoor 20417</p>
  <p class="info-title abs" style="left:110px;top:4363px">Message us</p>
  <p class="info-line abs" style="left:110px;top:4400px">hello@openmeadow.com<br>(+00) 555 0142</p>
  <div class="social abs" style="left:110px;top:4507px"><i></i><i></i><i></i></div>

  <div class="field abs" style="left:425px;top:4215px;width:315px">👤&nbsp;Name *</div>
  <div class="field abs" style="left:760px;top:4215px;width:315px">✉&nbsp;Email *</div>
  <div class="field abs" style="left:425px;top:4282px;width:650px">▯&nbsp;Phone number</div>
  <div class="field abs" style="left:425px;top:4350px;width:650px;height:98px;align-items:flex-start">Your message</div>
  <p class="abs" style="left:422px;top:4488px;width:440px;font-size:12px;line-height:1.6;color:#222">Lorem ipsum dolor sit amet, consectetur adipiscing elit, sed do eiusmod tempor incididunt ut labore et dolore</p>
  <a class="btn send abs">Send message</a>
</section>

<footer class="footer abs">
  <div class="brand abs" style="left:120px;top:100px"><i></i>Open meadow</div>
  <div class="footer-contact abs">
    <div><svg width="14" height="18" fill="none" stroke="#ddd" stroke-width="1.5"><path d="M7 17s6-6 6-10A6 6 0 001 7c0 4 6 10 6 10z"/><circle cx="7" cy="7" r="2"/></svg><span>7 Larchway Lane,<br>Fernhollow, 30981</span></div>
    <div><svg width="16" height="16" fill="none" stroke="#ddd" stroke-width="1.5"><path d="M3 1h3l2 4-2 1a9 9 0 004 4l1-2 4 2v3a2 2 0 01-2 2A13 13 0 011 3a2 2 0 012-2z"/></svg><span>+00 (555) 010-2233</span></div>
    <div><svg width="16" height="12" fill="none" stroke="#ddd" stroke-width="1.5"><rect x="1" y="1" width="14" height="10"/><path d="M1 1l7 6 7-6"/></svg><span>team@openmeadow.com</span></div>
  </div>
  <div class="f-col abs" style="left:393px;top:70px"><h4>INFORMATION</h4><ul><li>About Us</li><li>Latest Products</li><li>Product of the day!</li><li>Advertising</li><li>Contact Us</li></ul></div>
  <div class="f-col abs" style="left:668px;top:70px"><h4>MY ACCOUNT</h4><ul><li>My Account</li><li>Login/Register</li><li>Cart</li><li>Wishlist</li><li>Order History</li></ul></div>
  <div class="f-col abs" style="left:943px;top:70px"><h4>Quick Links</h4><ul><li>FAQs</li><li>Terms</li><li>Privacy Policy</li><li>Sitemap</li><li>Contact</li></ul></div>
  <div class="social abs" style="left:118px;top:385px;gap:18px"><i></i><i></i><i></i><i></i><i></i><i></i></div>
  <p class="copy abs">© 2020 COMPANY NAME. ALL RIGHTS RESERVED.</p>
  <div class="cards abs"><i></i><i></i><i></i><i></i></div>
</footer>

</body>
</html>
```